Pipelining Product Supply Company Needs New Stationery

We need new stationery (letter head, with compliments slips & business card) for our industry leading pipe lining supply company. basically we sell product to other plumbers to carry out pipe relining.

Im looking for something, fresh, professional, sleek and modern at the same time.

Ive attached a copy of the logo and also some guidelines to follow for colours and fonts etc.

Target Market(s)

Plumbers

Industry/Entity Type

Plumbing

Font styles to use
Sans Serif

Requirements
Must have
• The logo, space for ABN, Address, Phone Number, website and email.
Nice to have
• Stand out from the crowd. To look sleep and professional.
Should not have
• Any other colours apart from what is on the guidelines.

```html
<!DOCTYPE html>
<html lang="en">
<head>
<meta charset="utf-8">
<title>Reline Supply Co – Stationery</title>
<link href="https://fonts.googleapis.com/css2?family=Roboto:wght@400;700;900&display=swap" rel="stylesheet">
<style>
:root{
  --lime:#80ff00;
  --lime-pale:#e8fcd9;
  --lime-faint:#dcf9c4;
  --forest:#2f8c00;
  --ink:#6f6f6f;
  --rule:#9a9a9a;
  --paper:#ffffff;
  --bg-light:#ffffff;
  --bg-dark:#c9c9c9;
}
*{margin:0;padding:0;box-sizing:border-box}
html,body{width:1200px;height:1200px;overflow:hidden}
body{
  position:relative;
  font-family:"Roboto",Arial,sans-serif;
  background:radial-gradient(circle at 50% 52%,var(--bg-light) 0,var(--bg-light) 38%,var(--bg-dark) 100%);
}
.sheet{position:absolute;background:var(--paper);overflow:hidden;box-shadow:0 0 2px rgba(0,0,0,.12)}
.letterhead{left:95px;top:195px;width:508px;height:711px}
.comp-slip{left:620px;top:195px;width:508px;height:248px}
.card-front{left:620px;top:472px;width:215px;height:142px;background:var(--lime)}
.card-back{left:913px;top:472px;width:215px;height:142px}

.brand-name{font-weight:900;color:var(--forest);letter-spacing:.5px;line-height:1;white-space:nowrap}
.header-rule{position:absolute;height:7px;background:var(--lime)}
.faint-mark{position:absolute;font-weight:900;color:var(--lime-faint);line-height:1;white-space:nowrap}

.footer-contacts{position:absolute;display:flex;gap:9px;align-items:center;font-size:7px;font-weight:700;color:var(--ink);white-space:nowrap}
.footer-contacts span{display:flex;align-items:center;gap:3px}
.footer-contacts svg{width:7px;height:7px;fill:var(--ink)}
.footer-line{position:absolute;height:1px;background:var(--rule)}
.footer-band{position:absolute;background:var(--lime)}
.footer-url{position:absolute;color:#fff;font-weight:700;display:flex;align-items:center;justify-content:center;background:var(--lime)}

/* letterhead */
.letterhead .header-rule{left:0;right:0;top:42px}
.letterhead .brand-name{
  position:absolute;left:50%;top:36px;transform:translateX(-50%);
  padding:0 12px;background:var(--paper);font-size:17px;line-height:19px;
}
.letterhead .faint-mark{right:10px;bottom:34px;font-size:150px}
.letterhead .footer-contacts{left:18px;bottom:16px}
.letterhead .footer-line{left:0;width:340px;bottom:12px}
.letterhead .footer-band{left:0;right:0;bottom:0;height:12px}
.letterhead .footer-url{right:0;bottom:0;width:160px;height:34px;font-size:11px}

/* compliments slip */
.comp-slip .brand-name{position:absolute;left:50px;top:26px;font-size:15px}
.comp-slip .header-rule.left{left:0;top:34px;width:44px}
.comp-slip .header-rule.right{left:198px;right:0;top:34px}
.comp-slip .faint-mark{right:16px;bottom:26px;font-size:92px}
.comp-slip .footer-contacts{left:18px;bottom:12px}
.comp-slip .footer-line{left:0;width:340px;bottom:9px}
.comp-slip .footer-band{left:0;right:0;bottom:0;height:9px}
.comp-slip .footer-url{right:0;bottom:0;width:160px;height:28px;font-size:11px}

/* card front */
.card-front .brand-name{position:absolute;left:0;width:100%;top:50px;text-align:center;font-size:17px;color:#fff}
.card-front .web-strip{position:absolute;left:0;right:0;bottom:0;height:22px;background:var(--lime-pale);display:flex;align-items:flex-start;justify-content:center}
.card-front .web-strip span{display:block;margin-top:-4px;padding:2px 6px;background:var(--lime);color:#fff;font-size:8px;font-weight:700}

/* card back */
.card-back .brand-name{position:absolute;left:18px;top:52px;font-size:10px;line-height:12px}
.card-back .divider{position:absolute;left:104px;top:22px;width:1px;height:62px;background:var(--lime)}
.contact-list{position:absolute;left:112px;top:20px;list-style:none;font-size:5px;font-weight:700;color:var(--ink);line-height:1.3}
.contact-list li{display:flex;gap:4px;align-items:flex-start;margin-bottom:4px}
.contact-list svg{width:6px;height:6px;fill:var(--ink);flex:none}
.card-back .faint-mark{right:14px;bottom:14px;font-size:36px}
.card-back .footer-band{left:0;right:0;bottom:0;height:13px}
</style>
</head>
<body>

<svg width="0" height="0" style="position:absolute" aria-hidden="true">
  <symbol id="icon-pin" viewBox="0 0 10 10"><path d="M5 0a3.5 3.5 0 0 0-3.5 3.5C1.5 6 5 10 5 10s3.5-4 3.5-6.5A3.5 3.5 0 0 0 5 0zm0 5a1.5 1.5 0 1 1 0-3 1.5 1.5 0 0 1 0 3z"/></symbol>
  <symbol id="icon-phone" viewBox="0 0 10 10"><path d="M1 1h3v1.5L3 3.5l3.5 3.5 1-1H9v3H7.5C3.9 9 1 6.1 1 2.5z"/></symbol>
  <symbol id="icon-mail" viewBox="0 0 10 10"><path d="M5 0a5 5 0 1 0 2.5 9.3l-.5-.9A4 4 0 1 1 9 5v.6c0 .6-.4 1-.9 1s-.9-.4-.9-1V5A2.2 2.2 0 1 0 6.6 6.6 1.9 1.9 0 0 0 10 5.6V5A5 5 0 0 0 5 0zm0 6.2a1.2 1.2 0 1 1 0-2.4 1.2 1.2 0 0 1 0 2.4z"/></symbol>
  <symbol id="icon-web" viewBox="0 0 10 10"><path d="M5 0a5 5 0 1 0 0 10A5 5 0 0 0 5 0zm3.9 4.5H7.2a7 7 0 0 0-.8-3.3 4 4 0 0 1 2.5 3.3zM5 1.1c.6.8 1.1 2 1.2 3.4H3.8C3.9 3.1 4.4 1.9 5 1.1zM3.6 1.2a7 7 0 0 0-.8 3.3H1.1a4 4 0 0 1 2.5-3.3zM1.1 5.5h1.7a7 7 0 0 0 .8 3.3 4 4 0 0 1-2.5-3.3zM5 8.9c-.6-.8-1.1-2-1.2-3.4h2.4C6.1 6.9 5.6 8.1 5 8.9zm1.4-.1a7 7 0 0 0 .8-3.3h1.7a4 4 0 0 1-2.5 3.3z"/></symbol>
</svg>

<section class="sheet letterhead" aria-label="Letterhead">
  <div class="header-rule"></div>
  <div class="brand-name">RELINE SUPPLY CO</div>
  <div class="faint-mark" aria-hidden="true">RSC</div>
  <div class="footer-line"></div>
  <div class="footer-band"></div>
  <div class="footer-contacts">
    <span><svg><use href="#icon-pin"/></svg>12 Harbour Lane Riverton NSW 2100</span>
    <span><svg><use href="#icon-phone"/></svg>1-300-555-018</span>
    <span><svg><use href="#icon-mail"/></svg>sales@relinesupplyco.com.au</span>
  </div>
  <div class="footer-url">relinesupplyco.com.au</div>
</section>

<section class="sheet comp-slip" aria-label="Compliments slip">
  <div class="header-rule left"></div>
  <div class="header-rule right"></div>
  <div class="brand-name">RELINE SUPPLY CO</div>
  <div class="faint-mark" aria-hidden="true">RSC</div>
  <div class="footer-line"></div>
  <div class="footer-band"></div>
  <div class="footer-contacts">
    <span><svg><use href="#icon-pin"/></svg>12 Harbour Lane Riverton NSW 2100</span>
    <span><svg><use href="#icon-phone"/></svg>1-300-555-018</span>
    <span><svg><use href="#icon-mail"/></svg>sales@relinesupplyco.com.au</span>
  </div>
  <div class="footer-url">relinesupplyco.com.au</div>
</section>

<section class="sheet card-front" aria-label="Business card front">
  <div class="brand-name">RELINE SUPPLY CO</div>
  <div class="web-strip"><span>relinesupplyco.com.au</span></div>
</section>

<section class="sheet card-back" aria-label="Business card back">
  <div class="brand-name">RELINE<br>SUPPLY CO</div>
  <div class="divider"></div>
  <ul class="contact-list">
    <li><svg><use href="#icon-pin"/></svg><span>12 Harbour Lane, Riverton,<br>NSW 2100</span></li>
    <li><svg><use href="#icon-phone"/></svg><span>1-300-555-018</span></li>
    <li><svg><use href="#icon-mail"/></svg><span>sales@relinesupplyco.com.au</span></li>
    <li><svg><use href="#icon-web"/></svg><span>relinesupplyco.com.au</span></li>
  </ul>
  <div class="faint-mark" aria-hidden="true">RSC</div>
  <div class="footer-band"></div>
</section>

</body>
</html>
```